Business Card Design

Business Card for professional consulting firm working with large financial institutions.

Target Market(s)

Executive buyers

Industry/Entity Type

Banking

Contact Information for Business Card

Mild creativity wanted. Not boring, but do elaborate artwork.

Font styles to use
Serif
Sans Serif

Colors

Designer to choose colors to be used in the design.

Requirements
Must have
• Standard business card features - company name, individual name, telephone, website, email, locations.
Nice to have
• Two colors
Should not have
• too many colors, fancy printing, cartoons.

```html
<!DOCTYPE html>
<html lang="en">
<head>
<meta charset="utf-8">
<title>Northvane Advisory – Business Card</title>
<link rel="stylesheet" href="https://fonts.googleapis.com/css2?family=Lato:wght@400;700&display=swap">
<style>
  :root {
    --stage: #1c1c1e;
    --card-blue: #06308c;
    --card-black: #141415;
    --brand-blue: #1d3fae;
    --text-light: #d9dbe0;
    --text-muted: #9a9ca2;
    --rule: #c9cbd0;
  }
  * { margin: 0; padding: 0; box-sizing: border-box; }
  html, body {
    width: 1200px; height: 900px; overflow: hidden;
    background: var(--stage);
    font-family: "Lato", Arial, sans-serif;
  }
  .stage {
    position: relative; width: 1200px; height: 900px;
  }
  .card {
    position: absolute; left: 320px;
    width: 560px; height: 320px;
    border-radius: 22px;
    box-shadow: 0 18px 40px rgba(0,0,0,.55);
    overflow: hidden;
  }
  .card--front {
    top: 110px;
    background: linear-gradient(160deg, #0a3aa3 0%, var(--card-blue) 100%);
    display: flex; align-items: center; justify-content: center;
  }
  .card--front .brand-name {
    color: #ffffff; font-size: 40px; font-weight: 400; letter-spacing: .5px;
  }
  .card--back {
    top: 470px;
    background: var(--card-black);
  }
  .card--back .brand-name {
    position: absolute; right: 40px; top: 48px;
    color: var(--brand-blue); font-size: 26px; font-weight: 400;
  }
  .divider {
    position: absolute; left: 210px; right: 40px; top: 118px;
    height: 1px; background: var(--rule); opacity: .8;
  }
  .person {
    position: absolute; left: 40px; top: 142px;
  }
  .person__name {
    color: var(--brand-blue); font-size: 22px; font-weight: 400;
    text-transform: uppercase; letter-spacing: .5px;
  }
  .person__role {
    color: var(--text-muted); font-size: 16px; margin-top: 2px;
  }
  .address {
    position: absolute; left: 40px; top: 232px;
    color: var(--text-light); font-size: 18px; line-height: 1.3;
  }
  .contacts {
    position: absolute; right: 40px; top: 140px;
    list-style: none; text-align: right;
  }
  .contacts li {
    display: flex; justify-content: flex-end; align-items: center;
    gap: 8px; color: var(--text-light); font-size: 16px; line-height: 24px;
  }
  .contacts svg { width: 14px; height: 14px; fill: var(--brand-blue); }
</style>
</head>
<body>
<main class="stage">
  <section class="card card--front" aria-label="Card front">
    <span class="brand-name">Northvane Advisory</span>
  </section>

  <section class="card card--back" aria-label="Card back">
    <span class="brand-name">Northvane Advisory</span>
    <div class="divider"></div>
    <div class="person">
      <p class="person__name">Daniel Carter</p>
      <p class="person__role">Managing Director</p>
    </div>
    <p class="address">48 Harbour Lane, Suite 7<br>Eastbridge, 560210.</p>
    <ul class="contacts">
      <li>044-987 654 321
        <svg viewBox="0 0 16 16" aria-hidden="true"><path d="M3 1h3l1.5 4-2 1.2a9 9 0 0 0 4.3 4.3L11 8.5l4 1.5v3a2 2 0 0 1-2 2A12 12 0 0 1 1 3a2 2 0 0 1 2-2z"/></svg>
      </li>
      <li>hello@northvane.co
        <svg viewBox="0 0 16 16" aria-hidden="true"><path d="M1 3h14v10H1z M1 3l7 6 7-6" stroke="#141415" stroke-width="1.2"/></svg>
      </li>
      <li>www.northvane.co
        <svg viewBox="0 0 16 16" aria-hidden="true"><circle cx="8" cy="8" r="7"/><path d="M1 8h14M8 1c-3 4-3 10 0 14M8 1c3 4 3 10 0 14" stroke="#141415" stroke-width="1" fill="none"/></svg>
      </li>
    </ul>
  </section>
</main>
</body>
</html>
```